New Graphic Design Project / Email signiture and Letterhead

I would like a new SIMPLE but high end quality modern/heavy industrial design for an email Signiture and letter head that incorporates product photos or illustrations of our products to show our customers our range of products and also show our head office in Perth Western Australia and also our Australian and international reseller locations.
in my present email signature you would see that I have other company logos these companies are old partners of ours but some are no longer so I would like to have the option to add and change them if things change in the future.
for ideas Our main products are as follows
Composite Hose
Convoluted hose
Metal expansion joints
Fabric expansion joints
Rubber Expansion joints
Please see our website for ideas and our product photos.
www.dravoline.com.au
if you need any further information please let me know
i have attached our old email signiture for reference.
Mark

Target Market(s)

Oil and Gas / Mining / Petroleum and Chemical Refineries, high end engineering

Requirements
Must have
• pictures / photos of our core products and our company capabilities to show our existing and new customers what we can do.
in the email signature - links to company face book and LinkedIn, our website
I would like to have spaces for my company partners logos and need the final file to be in a format for me to change and update all details
All so our Font is Conthrax SB
Nice to have
• the email signature, I would like this to have all the required information ( as per attached present email signature ) but also be informative / marketing to show customers what we do if possible.
the letter head can be based from the same but simple with or without product photos

```html
<!DOCTYPE html>
<html lang="en">
<head>
<meta charset="utf-8">
<title>Dravoline Letterhead</title>
<link href="https://fonts.googleapis.com/css2?family=Montserrat:wght@300;400;500;700&display=swap" rel="stylesheet">
<style>
  :root {
    --ink: #2f3b48;
    --ink-dark: #1d1f22;
    --band: #2f3a44;
    --paper: #ffffff;
    --ghost: #f3f4f5;
  }
  * { margin: 0; padding: 0; box-sizing: border-box; }
  html, body { width: 847px; height: 1200px; overflow: hidden; background: var(--paper); }
  body { font-family: "Montserrat", sans-serif; color: var(--ink); }
  .letterhead { position: relative; width: 847px; height: 1200px; overflow: hidden; background: var(--paper); }

  .top-rule { position: absolute; left: 732px; top: 0; width: 3px; height: 62px; background: var(--band); }

  .brand { position: absolute; left: 99px; top: 71px; display: flex; align-items: center; gap: 22px; }
  .brand-dot { width: 84px; height: 84px; border-radius: 50%; border: 9px solid var(--ink-dark); }
  .brand-name { font-weight: 700; font-size: 42px; letter-spacing: 1px; color: var(--ink-dark); }

  .contact { position: absolute; right: 105px; top: 66px; list-style: none; }
  .contact li { display: flex; align-items: center; justify-content: flex-end; gap: 9px; font-size: 10.5px; line-height: 12px; color: var(--ink); margin-bottom: 9px; text-align: right; }
  .contact li.address { font-size: 9.5px; line-height: 11px; }
  .contact .icon { flex: none; width: 18px; height: 18px; border-radius: 50%; background: var(--band); display: flex; align-items: center; justify-content: center; }
  .contact .icon svg { width: 10px; height: 10px; fill: #fff; }

  .watermark { position: absolute; left: 309px; top: 507px; width: 250px; height: 250px; border-radius: 50%; border: 14px solid var(--ghost); }

  .headline { position: absolute; left: 96px; top: 258px; font-size: 44px; font-weight: 400; color: var(--ink); letter-spacing: -0.5px; }

  .body-copy { position: absolute; left: 101px; top: 318px; width: 640px; font-size: 19.5px; line-height: 24px; }
  .body-copy p { margin-bottom: 24px; }
  .body-copy .line { display: block; text-align: justify; text-align-last: justify; white-space: nowrap; overflow: visible; }

  .signoff { position: absolute; right: 106px; top: 934px; text-align: right; font-size: 16.5px; line-height: 21px; color: var(--ink); }

  .footer-band { position: absolute; left: 0; top: 1159px; width: 847px; height: 41px; background: var(--band); }
  .footer-band svg { position: absolute; left: 0; top: 0; }
  .footer-regions { position: absolute; left: 0; width: 847px; top: 3px; text-align: center; font-size: 25px; font-weight: 300; color: #fff; letter-spacing: 0.3px; }
</style>
</head>
<body>
<div class="letterhead">
  <div class="top-rule"></div>

  <div class="brand">
    <div class="brand-dot"></div>
    <div class="brand-name">DRAVOLINE</div>
  </div>

  <ul class="contact">
    <li><span>+614 0400 218 654<br>+618 9400 3172</span>
      <span class="icon"><svg viewBox="0 0 24 24"><path d="M6.6 10.8a15.1 15.1 0 0 0 6.6 6.6l2.2-2.2a1 1 0 0 1 1-.25 11.4 11.4 0 0 0 3.6.57 1 1 0 0 1 1 1V20a1 1 0 0 1-1 1A17 17 0 0 1 3 4a1 1 0 0 1 1-1h3.5a1 1 0 0 1 1 1c0 1.25.2 2.45.57 3.57a1 1 0 0 1-.25 1z"/></svg></span></li>
    <li><span>mark@dravoline.com.au</span>
      <span class="icon"><svg viewBox="0 0 24 24"><path d="M3 6h18v12H3z M3 6l9 7 9-7" stroke="#2f3a44" stroke-width="1.5"/></svg></span></li>
    <li><span>www.dravoline.com.au</span>
      <span class="icon"><svg viewBox="0 0 24 24"><path d="M3 4h18v12H3zM10 16h4v3h3v2H7v-2h3z"/></svg></span></li>
    <li class="address"><span>42 Harlow Street<br>Kelmscott, WA 6111</span>
      <span class="icon"><svg viewBox="0 0 24 24"><path d="M12 3l9 8h-3v9h-4v-6h-4v6H6v-9H3z"/></svg></span></li>
  </ul>

  <div class="watermark" aria-hidden="true"></div>

  <h1 class="headline">SUBJECT HEADLINE HERE</h1>

  <div class="body-copy">
    <p>
      <span class="line">Lorem ipsum dolor sit amet, consectetuer adipiscing</span>
      <span class="line">elit, sed diam nonummy nibh euismod tincidunt</span>
      <span class="line">ut laoreet dolore magna aliquam erat volutpat.</span>
    </p>
    <p>
      <span class="line">Ut wisi enim ad minim veniam, quis nostrud exerci tation ullamcor-</span>
      <span class="line">per suscipit lobortis nisl ut aliquip ex ea commodo consequat.</span>
      <span class="line">Duis autem vel eum iriure dolor in hendrerit in vulputate velit esse</span>
      <span class="line">molestie consequat, vel illum dolore eu feugiat nulla facilisis at</span>
      <span class="line">vero eros et accumsan et iusto odio dignissim qui blandit praesent</span>
      <span class="line">luptatum zzril delenit augue duis dolore te feugait nulla facilisi.</span>
    </p>
    <p>
      <span class="line">Lorem ipsum dolor sit amet, cons ectetuer adipiscing</span>
      <span class="line">elit, sed diam nonummy nibh euismod tincidunt</span>
    </p>
    <p>
      <span class="line">vel illum dolore eu feugiat nulla facilisis at vero eros et</span>
      <span class="line">accumsan et iusto odio dignissim qui blandit praesent</span>
      <span class="line">luptatum zzril delenit augue duis dolore te feugait nulla facilisi.</span>
    </p>
    <p>
      <span class="line">Ut wisi enim ad minim veniam, quis nostrud exerci tation</span>
      <span class="line">ullamcorper suscipit lobortis nisl ut aliquip ex ea commodo conse-</span>
      <span class="line">quat. Duis autem vel eum iriure dolor in hendrerit in vulputate</span>
    </p>
  </div>

  <div class="signoff">
    Creative Art Director<br>
    Pellenissque id neque ligula, Nullam Posuere<br>
    www.companynamehere.om
  </div>

  <div class="footer-band">
    <svg width="847" height="41" viewBox="0 0 847 41" aria-hidden="true">
      <polygon points="131,0 138,0 123,41 116,41" fill="#fff"/>
      <polygon points="146,0 153,0 138,41 131,41" fill="#fff"/>
      <polygon points="706,0 713,0 698,41 691,41" fill="#fff"/>
      <polygon points="721,0 728,0 713,41 706,41" fill="#fff"/>
    </svg>
    <div class="footer-regions">Australia, Singapure, Indonesia, Vietnam</div>
  </div>
</div>
</body>
</html>
```